Local Directory Ad

We currently have an advertisement in our local directory (see attached). We would like to make it look more appealing.
Dimensions are 110mm H X 175mm W
We would like to keep the same colours and contact details remain the same.
Most of the content can remain the same, Just remove the line Tax effective remote area salary packaging and add in Self Managed Super Funds.We want to change mortgage broking to Mortgage Broking and Loan Structuring.

We want to change the line Local accountants Local Knowledge Local Experience - to something like local knowledge beyond compare or unsurpassed local knowledge but open to suggestions on this.

there are some good designs posted so far. I particulalry like the ones from marloquip, tovel58, and the last one posted by pruvsomlak and WPH. Keep up the good work guys

```html
<!DOCTYPE html>
<html lang="en">
<head>
<meta charset="utf-8">
<title>Brindle Accounting &amp; Finance – Directory Ad</title>
<link rel="stylesheet" href="https://fonts.googleapis.com/css2?family=Tinos:wght@700&family=Source+Sans+3:wght@400;700&display=swap">
<style>
  :root {
    --backdrop: #2a2a2a;
    --header-dark: #3a3533;
    --brand-red: #b01e2e;
    --ink: #333333;
    --paper: #ffffff;
    --name-light: #eeeae4;
    --muted: #9a9590;
    --bullet: #3b3b3b;
  }
  * { box-sizing: border-box; margin: 0; padding: 0; }
  html, body { width: 1200px; height: 1000px; overflow: hidden; }
  body { background: var(--backdrop); position: relative; font-family: "Source Sans 3", sans-serif; }

  .ad {
    position: absolute; left: 115px; top: 184px;
    width: 990px; height: 621px;
    background: var(--paper); overflow: hidden;
  }

  .masthead {
    position: absolute; left: 0; top: 0; width: 990px; height: 171px;
    background: var(--header-dark);
  }
  .brand-name {
    position: absolute; left: 0; top: 52px; width: 100%; text-align: center;
    font-family: "Source Sans 3", sans-serif; font-weight: 400;
    font-size: 54px; line-height: 60px; color: var(--name-light);
  }
  .licence {
    position: absolute; right: 6px; top: 151px;
    font-size: 14px; color: var(--muted);
  }

  .photo-area { position: absolute; left: 535px; top: 171px; width: 455px; height: 342px; }

  .tagline {
    position: absolute; left: 10px; top: 195px;
    font-family: "Tinos", serif; font-weight: 700; font-size: 25px;
    color: var(--brand-red); letter-spacing: 0.5px; white-space: nowrap;
  }

  .service-panel { position: absolute; left: 0; top: 246px; width: 615px; height: 267px; }
  .service-intro {
    position: absolute; left: 9px; top: 254px;
    font-weight: 700; font-size: 23px; color: var(--paper); white-space: nowrap;
  }
  .service {
    position: absolute; font-size: 28px; line-height: 34px; color: var(--paper); white-space: nowrap;
  }
  .service::before {
    content: ""; display: inline-block; width: 12px; height: 12px;
    background: var(--bullet); margin-right: 8px; vertical-align: 4px;
  }

  .divider { position: absolute; left: 0; top: 512px; width: 990px; height: 4px; background: var(--header-dark); }

  .contact { position: absolute; font-size: 23px; color: var(--ink); line-height: 29px; white-space: nowrap; font-style: normal; }
  .contact-icon { position: absolute; }
</style>
</head>
<body>
  <main class="ad">
    <header class="masthead">
      <h1 class="brand-name">Brindle Accounting &amp; Finance</h1>
      <div class="licence">Australian Credit License 512 904</div>
    </header>

    <svg class="photo-area" viewBox="0 0 455 342" role="img" aria-label="Photo of an accountant's hands writing with a pen beside a calculator and financial papers">
      <defs>
        <linearGradient id="photoTone" x1="0" y1="0" x2="1" y2="1">
          <stop offset="0" stop-color="#c8d6e2"/>
          <stop offset="0.5" stop-color="#e6ecf1"/>
          <stop offset="1" stop-color="#b4c4d2"/>
        </linearGradient>
      </defs>
      <polygon points="40,0 455,0 455,342 75,342 0,75" fill="url(#photoTone)"/>
    </svg>

    <h2 class="tagline">LOCAL KNOWLEDGE BEYOND COMPARE</h2>

    <svg class="service-panel" viewBox="0 0 615 267" aria-hidden="true">
      <defs>
        <radialGradient id="redPanel" cx="0.55" cy="0.5" r="0.6">
          <stop offset="0" stop-color="#e0182f"/>
          <stop offset="1" stop-color="#b01e2e"/>
        </radialGradient>
      </defs>
      <polygon points="0,0 535,0 610,267 0,267" fill="url(#redPanel)"/>
    </svg>

    <p class="service-intro">We are here for you all year round to assist with...</p>
    <p class="service" style="left:9px; top:305px;">Accounting &amp; Taxation</p>
    <p class="service" style="left:321px; top:305px;">&nbsp;Bookkeeping</p>
    <p class="service" style="left:36px; top:357px;">GST and BAS’s</p>
    <p class="service" style="left:271px; top:357px;">Business Advice</p>
    <p class="service" style="left:95px; top:408px;">Self Managed Super Funds</p>
    <p class="service" style="left:34px; top:461px;">Mortgage Broking and Loan Structuring</p>

    <div class="divider"></div>

    <svg class="contact-icon" style="left:19px; top:533px;" width="48" height="74" viewBox="0 0 48 74" aria-hidden="true">
      <path d="M24 0C10.7 0 0 10.7 0 24c0 17 24 50 24 50s24-33 24-50C48 10.7 37.3 0 24 0z" fill="var(--brand-red)"/>
      <circle cx="24" cy="23" r="11" fill="#fff"/>
    </svg>
    <address class="contact" style="left:80px; top:525px;">
      Shop 3 Corella Arcade<br>12 Marlow St Tindalup<br>PO Box 418 Tindalup 6790
    </address>

    <svg class="contact-icon" style="left:440px; top:535px;" width="16" height="26" viewBox="0 0 16 26" aria-hidden="true">
      <path d="M5 1 L9 1 L10 7 L7 9 Q7 14 10 18 L13 17 L15 23 L11 25 Q2 20 2 9 Q2 3 5 1z" fill="var(--brand-red)"/>
    </svg>
    <p class="contact" style="left:473px; top:536px;">9081 4427</p>
    <svg class="contact-icon" style="left:437px; top:575px;" width="26" height="30" viewBox="0 0 26 30" aria-hidden="true">
      <rect x="6" y="0" width="14" height="8" fill="var(--brand-red)"/>
      <rect x="0" y="9" width="26" height="12" rx="2" fill="var(--brand-red)"/>
      <rect x="5" y="19" width="16" height="11" fill="var(--brand-red)" stroke="#fff" stroke-width="1.5"/>
      <line x1="8" y1="24" x2="18" y2="24" stroke="#fff" stroke-width="1.5"/>
    </svg>
    <p class="contact" style="left:473px; top:572px;">9081 4439</p>

    <svg class="contact-icon" style="left:679px; top:540px;" width="29" height="21" viewBox="0 0 29 21" aria-hidden="true">
      <rect x="1" y="1" width="27" height="19" fill="none" stroke="var(--brand-red)" stroke-width="2"/>
      <polyline points="1,1 14.5,12 28,1" fill="none" stroke="var(--brand-red)" stroke-width="2"/>
    </svg>
    <p class="contact" style="left:720px; top:536px;">reception@bafx.com.au</p>
    <svg class="contact-icon" style="left:680px; top:577px;" width="27" height="27" viewBox="0 0 27 27" aria-hidden="true">
      <g fill="none" stroke="var(--brand-red)" stroke-width="1.6">
        <circle cx="13.5" cy="13.5" r="12"/>
        <ellipse cx="13.5" cy="13.5" rx="5.5" ry="12"/>
        <line x1="1.5" y1="13.5" x2="25.5" y2="13.5"/>
        <line x1="3.5" y1="7.5" x2="23.5" y2="7.5"/>
        <line x1="3.5" y1="19.5" x2="23.5" y2="19.5"/>
      </g>
    </svg>
    <p class="contact" style="left:724px; top:571px;">www.bafx.com.au</p>
  </main>
</body>
</html>
```